We want to design total new business card and logo for Kestrel Building Services Ltd

Our company name Kestrel Building Services Ltd. Design new logo and business card , need hi-end luxury style art for architecture and construction industry. The card should simple but stylish. Our business focus on CONNECT tradesman to construction company, help marketing construction company tender oversea projects, managing franchise in construction sector, delivery amazing services to our client, so Logo should show the CONNECTION IDEA, CONNECTING PEOPLE, LUXURY. Visit our website for more information: kestrelgroup-example.co.nz

Target Market(s)

Directors or managers

Industry/Entity Type

Construction Company

Contact Information for Business Card

Name, Title, Mobile, Email, Website

Font styles to use
Serif

Colors

Designer to choose colors to be used in the design.

Requirements
Must have
• Simple and luxury, connection icon
Nice to have
• Special materials, plastic card, look through,...
• Look new ideas.

```html
<!DOCTYPE html>
<html lang="en">
<head>
<meta charset="utf-8">
<title>Kestrel Building Services – Business Card</title>
<link href="https://fonts.googleapis.com/css2?family=Noticia+Text:wght@400;700&family=Oswald:wght@500&family=Merienda:wght@700&family=Arimo&display=swap" rel="stylesheet">
<style>
  :root {
    --backdrop: #cdc1b6;
    --card-fill: rgba(255, 255, 255, 0.38);
    --brand-cyan: #0fa9c8;
    --ink-dark: #1c1a19;
    --ink-brown: #4e4440;
    --band-text: #f1ede8;
  }
  html, body {
    margin: 0;
    padding: 0;
    width: 1200px;
    height: 960px;
    overflow: hidden;
    background: var(--backdrop);
  }
  .canvas {
    position: relative;
    width: 1200px;
    height: 960px;
  }
  .business-card {
    position: absolute;
    left: 333px;
    top: 306px;
    width: 583px;
    height: 348px;
    background: var(--card-fill);
    border-radius: 22px 4px 22px 0;
    overflow: hidden;
  }
  .holder-name {
    position: absolute;
    right: 382px;
    top: 44px;
    margin: 0;
    text-align: right;
    font-family: "Oswald", sans-serif;
    font-weight: 500;
    font-size: 38px;
    line-height: 1;
    letter-spacing: 1px;
    color: var(--brand-cyan);
  }
  .holder-title {
    position: absolute;
    right: 382px;
    top: 84px;
    text-align: right;
    font-family: "Oswald", sans-serif;
    font-size: 10px;
    letter-spacing: 0.5px;
    color: var(--brand-cyan);
  }
  .tagline {
    position: absolute;
    right: 18px;
    top: 38px;
    font-family: "Merienda", cursive;
    font-weight: 700;
    font-size: 12px;
    color: var(--ink-dark);
  }
  .contact {
    position: absolute;
    right: 338px;
    top: 178px;
    text-align: right;
    color: var(--brand-cyan);
  }
  .contact-phone {
    font-family: "Oswald", sans-serif;
    font-weight: 500;
    font-size: 23px;
    letter-spacing: 0.5px;
    line-height: 1.1;
  }
  .contact-line {
    display: flex;
    justify-content: space-between;
    gap: 12px;
    font-family: "Arimo", sans-serif;
    font-size: 12px;
    line-height: 19px;
  }
  .card-mark {
    position: absolute;
    left: 409px;
    top: 150px;
    width: 120px;
    height: 120px;
    background: var(--brand-cyan);
  }
  .brand-band {
    position: absolute;
    left: 0;
    bottom: 0;
    width: 100%;
    height: 62px;
    background: var(--brand-cyan);
    display: flex;
    align-items: center;
    justify-content: flex-end;
    padding-right: 12px;
    box-sizing: border-box;
  }
  .brand-band-name {
    font-family: "Noticia Text", serif;
    font-weight: 700;
    font-size: 30px;
    letter-spacing: 0.5px;
    color: var(--band-text);
  }
  .signature-mark {
    position: absolute;
    left: 884px;
    top: 768px;
    width: 80px;
    height: 80px;
    background: var(--ink-brown);
  }
  .brand-signature {
    position: absolute;
    right: 64px;
    top: 862px;
    margin: 0;
    font-family: "Noticia Text", serif;
    font-weight: 700;
    font-size: 30px;
    letter-spacing: 0.5px;
    color: var(--ink-brown);
  }
</style>
</head>
<body>
<main class="canvas">
  <section class="business-card" aria-label="Business card">
    <h1 class="holder-name">MARCUS</h1>
    <div class="holder-title">DIRECTION</div>
    <div class="tagline">Amazing Services Affordable Price</div>
    <div class="contact">
      <div class="contact-phone">0800 555 0142</div>
      <div class="contact-line"><span>E:</span><span>reid@kestrelgroup-example.co.nz</span></div>
      <div class="contact-line"><span>W:</span><span>www.kestrelgroup-example.co.nz</span></div>
    </div>
    <div class="card-mark" aria-hidden="true"></div>
    <div class="brand-band">
      <span class="brand-band-name">KESTREL BUILDING SERVICES</span>
    </div>
  </section>
  <div class="signature-mark" aria-hidden="true"></div>
  <p class="brand-signature">KESTREL BUILDING SERVICES</p>
</main>
</body>
</html>
```